Need standup pouch design (Sri Lankan theme) for True Ceylon Cinnamon with MCT Oil:
- Organic
- 100% Vegetarian
- GMO Free
- Gluten Free
- 3rd Party Tested

```html
<!DOCTYPE html>
<html lang="en">
<head>
<meta charset="utf-8">
<title>True Ceylon Cinnamon Pouch Label</title>
<link href="https://fonts.googleapis.com/css2?family=Alegreya+Sans+SC:wght@800;900&family=Oswald:wght@500;600&display=swap" rel="stylesheet">
<style>
  :root {
    --orange: #f7941d;
    --orange-deep: #ea6b1f;
    --green: #0d5e56;
    --green-dark: #084a43;
    --red: #e0462e;
    --cream: #fce3be;
    --brown: #a4583a;
    --stage: #c9c9c9;
  }
  html, body {
    margin: 0;
    padding: 0;
    width: 1200px;
    height: 2317px;
    overflow: hidden;
    background: var(--stage);
  }
  .label {
    position: absolute;
    left: 100px;
    top: 350px;
    width: 1000px;
    height: 1618px;
    background: var(--orange);
    overflow: hidden;
    box-shadow: 0 12px 30px rgba(0,0,0,.25);
  }
  .label-art {
    position: absolute;
    inset: 0;
    width: 1000px;
    height: 1618px;
  }
  .headline {
    position: absolute;
    left: 0;
    width: 1000px;
    text-align: center;
    font-family: "Alegreya Sans SC", sans-serif;
    font-weight: 900;
    line-height: 1;
    margin: 0;
    white-space: nowrap;
  }
  .headline-true { top: 420px; font-size: 58px; color: var(--green); }
  .headline-ceylon { top: 470px; font-size: 112px; color: var(--green); letter-spacing: 1px; }
  .headline-cinnamon {
    top: 575px; font-size: 142px; color: var(--red); letter-spacing: 1px;
    text-shadow: 4px 4px 0 #f4b98a;
  }
  .headline-mct {
    top: 707px; font-size: 62px; color: var(--red);
    text-shadow: 3px 3px 0 #f4b98a;
  }
  .grade {
    position: absolute;
    top: 812px; left: 0; width: 1000px;
    text-align: center;
    font-family: "Alegreya Sans SC", sans-serif;
    font-weight: 800;
    font-size: 46px;
    line-height: 1;
    color: var(--cream);
    margin: 0;
    white-space: nowrap;
  }
  .brand-name {
    position: absolute;
    top: 200px; left: 0; width: 1000px;
    text-align: center;
    font-family: "Alegreya Sans SC", sans-serif;
    font-weight: 900;
    font-size: 34px;
    line-height: 1;
    color: var(--cream);
    margin: 0;
    white-space: nowrap;
  }
  .badge-text {
    position: absolute;
    width: 178px;
    text-align: center;
    font-family: "Oswald", sans-serif;
    font-weight: 500;
    line-height: 1;
    color: var(--cream);
  }
  .badge-text strong { display: block; font-size: 46px; font-weight: 600; }
  .badge-text span { display: block; font-size: 26px; margin-top: 4px; }
  .badge-origin { left: 48px; top: 400px; }
  .badge-organic { left: 779px; top: 418px; }
  .species {
    position: absolute;
    top: 1450px; left: 200px; width: 560px;
    text-align: center;
    font-family: "Oswald", sans-serif;
    font-weight: 500;
    font-size: 22px;
    line-height: 1;
    letter-spacing: 9px;
    color: var(--cream);
    margin: 0;
    white-space: nowrap;
  }
  .net-weight {
    position: absolute;
    left: 790px; top: 1440px;
    width: 130px; height: 138px;
    box-sizing: border-box;
    border: 4px solid var(--cream);
    border-radius: 8px;
    text-align: center;
    font-family: "Oswald", sans-serif;
    font-weight: 500;
    color: var(--cream);
    line-height: 1;
    white-space: nowrap;
  }
  .net-weight .net-label { display: block; font-size: 32px; margin-top: 12px; }
  .net-weight .net-value { display: block; font-size: 52px; margin-top: 8px; }
  .icon-text { font-family: "Oswald", sans-serif; font-weight: 600; font-size: 11px; fill: var(--cream); letter-spacing: 1px; }
  .banner-text { font-family: "Oswald", sans-serif; font-weight: 600; font-size: 54px; fill: var(--cream); }
</style>
</head>
<body>
<main class="label">
  <svg class="label-art" viewBox="0 0 1000 1618" xmlns="http://www.w3.org/2000/svg">
    <defs>
      <linearGradient id="sceneGrad" x1="0" y1="0" x2="0" y2="1">
        <stop offset="0" stop-color="#f7941d"/>
        <stop offset="0.45" stop-color="#ea6b1f"/>
        <stop offset="0.8" stop-color="#0d5e56"/>
      </linearGradient>
      <radialGradient id="ornamentGrad" cx="0.5" cy="0.5" r="0.5">
        <stop offset="0" stop-color="#0d5e56"/>
        <stop offset="0.6" stop-color="#e0462e"/>
        <stop offset="1" stop-color="#f4a06a"/>
      </radialGradient>
      <linearGradient id="quillGrad" x1="0" y1="0" x2="1" y2="1">
        <stop offset="0" stop-color="#c0714c"/>
        <stop offset="1" stop-color="#7a3b24"/>
      </linearGradient>
      <path id="arcTop" d="M-28 0 A28 28 0 0 1 28 0"/>
      <path id="bannerLine" d="M205 1336 Q480 1448 800 1262"/>
    </defs>

    <path role="img" aria-label="Faint line ornament in the top left corner" d="M0 0 L300 0 A300 300 0 0 1 0 300 Z" fill="#fce3be" opacity="0.15"/>
    <circle role="img" aria-label="Sri Lankan mandala ornament, top right" cx="1000" cy="0" r="300" fill="url(#ornamentGrad)"/>

    <rect role="img" aria-label="Palm tree landscape with a pile of cinnamon powder, quills and cardamom" x="0" y="880" width="1000" height="430" fill="url(#sceneGrad)"/>
    <rect x="0" y="1300" width="1000" height="318" fill="var(--green)"/>
    <circle role="img" aria-label="Sri Lankan mandala ornament, bottom left" cx="0" cy="1618" r="270" fill="url(#ornamentGrad)"/>

    <ellipse cx="500" cy="219" rx="182" ry="102" fill="var(--cream)"/>
    <ellipse cx="500" cy="219" rx="170" ry="90" fill="var(--green)"/>

    <circle cx="137" cy="439" r="100" fill="none" stroke="var(--cream)" stroke-width="3" stroke-dasharray="6 6" opacity="0.7"/>
    <circle cx="137" cy="439" r="88" fill="var(--red)"/>
    <circle cx="868" cy="439" r="100" fill="none" stroke="var(--cream)" stroke-width="3" stroke-dasharray="6 6" opacity="0.7"/>
    <circle cx="868" cy="439" r="88" fill="var(--green)"/>
    <path d="M852 398 C852 375 872 364 890 362 C890 386 876 400 856 402 Z M856 404 L872 382" fill="var(--cream)" stroke="var(--green)" stroke-width="2"/>

    <path d="M218 570 C218 470 330 430 420 410 C470 395 490 372 500 345 C510 372 530 395 580 410 C670 430 782 470 782 570 Z" fill="var(--cream)" stroke="var(--red)" stroke-width="16"/>
    <path d="M218 570 C218 470 330 430 420 410 C470 395 490 372 500 345 C510 372 530 395 580 410 C670 430 782 470 782 570" fill="none" stroke="var(--cream)" stroke-width="5" stroke-linecap="round" stroke-dasharray="0 16"/>
    <rect x="40" y="551" width="913" height="229" fill="var(--cream)"/>
    <line x1="90" y1="736" x2="305" y2="736" stroke="var(--red)" stroke-width="4"/>
    <line x1="695" y1="736" x2="910" y2="736" stroke="var(--red)" stroke-width="4"/>

    <polygon points="175,836 212,800 820,800 857,836 820,872 212,872" fill="var(--green)" stroke="var(--cream)" stroke-width="4"/>

    <ellipse cx="497" cy="1170" rx="276" ry="180" fill="var(--cream)"/>
    <ellipse role="img" aria-label="Photo of Ceylon cinnamon quills" cx="497" cy="1170" rx="260" ry="164" fill="url(#quillGrad)"/>

    <path d="M185 1290 Q480 1400 790 1225 L815 1300 Q480 1480 210 1370 Z" fill="var(--red)" stroke="var(--cream)" stroke-width="5"/>
    <text class="banner-text" text-anchor="middle"><textPath href="#bannerLine" startOffset="50%">WHOLE QUILLS &amp; POWDER</textPath></text>

    <g transform="translate(323 1545)">
      <circle r="38" fill="none" stroke="var(--cream)" stroke-width="3"/>
      <text class="icon-text" text-anchor="middle"><textPath href="#arcTop" startOffset="50%">VEGAN</textPath></text>
      <text class="icon-text" text-anchor="middle" y="30">100%</text>
      <path d="M-10 12 C-14 -4 0 -16 14 -14 C14 4 2 14 -10 12 Z M-10 12 L6 -6" fill="none" stroke="var(--cream)" stroke-width="2.5"/>
    </g>
    <g transform="translate(440 1545)">
      <circle r="38" fill="none" stroke="var(--cream)" stroke-width="3"/>
      <text class="icon-text" text-anchor="middle"><textPath href="#arcTop" startOffset="50%">GLUTEN</textPath></text>
      <text class="icon-text" text-anchor="middle" y="30">FREE</text>
      <path d="M-12 14 L12 -14 M-4 4 L-10 -6 M2 -2 L-2 -12 M-4 4 L6 8 M2 -2 L12 2" fill="none" stroke="var(--cream)" stroke-width="2.5" stroke-linecap="round"/>
    </g>
    <g transform="translate(556 1545)">
      <circle r="38" fill="none" stroke="var(--cream)" stroke-width="3"/>
      <text class="icon-text" text-anchor="middle"><textPath href="#arcTop" startOffset="50%">GMO</textPath></text>
      <text class="icon-text" text-anchor="middle" y="30">FREE</text>
      <path d="M-5 -16 L-5 -4 L-13 14 L13 14 L5 -4 L5 -16 M-8 -16 L8 -16" fill="none" stroke="var(--cream)" stroke-width="2.5" stroke-linejoin="round"/>
    </g>
    <g transform="translate(674 1545)">
      <circle r="38" fill="none" stroke="var(--cream)" stroke-width="3"/>
      <text class="icon-text" text-anchor="middle"><textPath href="#arcTop" startOffset="50%">LAB</textPath></text>
      <text class="icon-text" text-anchor="middle" y="30">TESTED</text>
      <path d="M-12 14 L12 14 M-2 14 L-2 6 M-8 6 L6 6 M-4 6 L2 -14 L8 -12 L4 2" fill="none" stroke="var(--cream)" stroke-width="2.5" stroke-linejoin="round"/>
    </g>
  </svg>

  <p class="brand-name">Kandyra Spices</p>

  <div class="badge-text badge-origin"><strong>ORIGIN</strong><span>SRI LANKA</span></div>
  <div class="badge-text badge-organic"><strong>100%</strong><span>ORGANIC</span></div>

  <h1 class="headline headline-true">TRUE</h1>
  <p class="headline headline-ceylon">CEYLON</p>
  <p class="headline headline-cinnamon">CINNAMON</p>
  <p class="headline headline-mct">WITH MCT OIL</p>
  <p class="grade">PREMIUM GRANDE ALBA</p>

  <p class="species">CINNAMOMUM ZEYLANICUM</p>

  <div class="net-weight">
    <span class="net-label">NET WT</span>
    <span class="net-value">400G</span>
  </div>
</main>
</body>
</html>
```